Vel

I have the logo for the back already. Need the front to match.
Need a VEL logo which I can provide or you can download one - VEL Realty in canada... Back of the card will be my logo and name. Front will have the info...
I would like a black background. Match colors on front to the back..
Details on Card

Target Market(s)

Realestate clients.. Keep it classy like the logo

Contact Information for Business Card

Reena Dhot office - 4035550187 cell - 4035550264 email - Reena@ReenaDhot.Com. website - ReenaDhot.Com Facebook - RDhotRealty Instagram - Reena_Yyc_Realtor Address - 514 - 23 St NE | T3K5M8

Colors
3176b5
33a6d7
85cae6

Requirements
Must have
• same color scheme as the logo
logo will be on the back
Black Background
Horizontal card
The one side of the card should be clean. like I stated, just my logo " Reena Dhot " and nothing else

```html
<!DOCTYPE html>
<html lang="en">
<head>
<meta charset="utf-8">
<title>Reena Dhot – Business Cards</title>
<link href="https://fonts.googleapis.com/css2?family=Cinzel:wght@500&family=Montserrat:wght@400&display=swap" rel="stylesheet">
<style>
  :root {
    --canvas: #d9d9d9;
    --brand-blue: #1576b8;
    --brand-ink: #231f20;
    --logo-blue: #1a72b5;
    --icon-blue: #33a6d7;
    --card-white: #ffffff;
    --text-grey: #4a4a4a;
  }
  * { margin: 0; padding: 0; box-sizing: border-box; }
  html, body { width: 1200px; height: 1000px; overflow: hidden; }
  body { background: var(--canvas); position: relative; font-family: "Montserrat", sans-serif; }

  .card {
    position: absolute;
    width: 523px;
    height: 290px;
    box-shadow: 0 18px 28px rgba(0,0,0,0.28);
  }
  .card--blue  { left: 64px;  top: 141px; background: var(--brand-blue); }
  .card--black { left: 613px; top: 141px; background: var(--brand-ink); }
  .card--info-a { left: 64px;  top: 572px; background: var(--card-white); }
  .card--info-b { left: 613px; top: 572px; background: var(--card-white); }

  .brand-name {
    font-family: "Cinzel", serif;
    font-weight: 500;
    letter-spacing: 1px;
    white-space: nowrap;
    position: absolute;
  }
  .brand-name--hero {
    left: 0; right: 0; top: 118px;
    text-align: center;
    font-size: 44px;
  }
  .card--blue .brand-name--hero { color: #ffffff; }
  .card--black .brand-name--hero { color: var(--logo-blue); }

  .brand-name--small {
    left: 30px; width: 172px; top: 129px;
    text-align: center;
    font-size: 27px;
    color: var(--logo-blue);
  }

  .contact-list {
    position: absolute;
    left: 232px;
    top: 70px;
    list-style: none;
  }
  .contact-list li {
    display: flex;
    align-items: center;
    height: 22px;
    font-size: 16px;
    color: var(--text-grey);
  }
  .contact-icon {
    width: 19px; height: 19px;
    margin-right: 7px;
    flex: none;
  }
</style>
</head>
<body>

<section class="card card--blue">
  <div class="brand-name brand-name--hero">REENA DHOT</div>
</section>

<section class="card card--black">
  <div class="brand-name brand-name--hero">REENA DHOT</div>
</section>

<section class="card card--info-a">
  <div class="brand-name brand-name--small">REENA DHOT</div>
  <ul class="contact-list">
    <li><svg class="contact-icon" viewBox="0 0 20 20"><circle cx="10" cy="10" r="10" fill="#33a6d7"/><path d="M6.5 5.5l2 0 1 2.5-1.3 1a6 6 0 0 0 2.8 2.8l1-1.3 2.5 1v2a1 1 0 0 1-1 1A8 8 0 0 1 5.5 6.5a1 1 0 0 1 1-1z" fill="#fff"/></svg>Reena Dhot Office 4035550187</li>
    <li><svg class="contact-icon" viewBox="0 0 20 20"><circle cx="10" cy="10" r="10" fill="#33a6d7"/><path d="M6.5 5.5l2 0 1 2.5-1.3 1a6 6 0 0 0 2.8 2.8l1-1.3 2.5 1v2a1 1 0 0 1-1 1A8 8 0 0 1 5.5 6.5a1 1 0 0 1 1-1z" fill="#fff"/></svg>4035550264</li>
    <li><svg class="contact-icon" viewBox="0 0 20 20"><circle cx="10" cy="10" r="10" fill="#33a6d7"/><rect x="5" y="6.5" width="10" height="7" fill="none" stroke="#fff" stroke-width="1.2"/><path d="M5 6.5l5 4 5-4" fill="none" stroke="#fff" stroke-width="1.2"/></svg>Reena@ReenaDhot.Com</li>
    <li><svg class="contact-icon" viewBox="0 0 20 20"><circle cx="10" cy="10" r="10" fill="#33a6d7"/><circle cx="10" cy="10" r="5" fill="none" stroke="#fff" stroke-width="1.1"/><ellipse cx="10" cy="10" rx="2.2" ry="5" fill="none" stroke="#fff" stroke-width="1.1"/><path d="M5 10h10" stroke="#fff" stroke-width="1.1"/></svg>ReenaDhot.Com</li>
    <li><svg class="contact-icon" viewBox="0 0 20 20"><circle cx="10" cy="10" r="10" fill="#33a6d7"/></svg>RDhotRealty</li>
    <li><svg class="contact-icon" viewBox="0 0 20 20"><circle cx="10" cy="10" r="10" fill="#33a6d7"/></svg>Reena_Yyc_Realtor</li>
    <li><svg class="contact-icon" viewBox="0 0 20 20"><circle cx="10" cy="10" r="10" fill="#33a6d7"/><path d="M10 4.5a3.8 3.8 0 0 1 3.8 3.8c0 2.8-3.8 7-3.8 7s-3.8-4.2-3.8-7A3.8 3.8 0 0 1 10 4.5z" fill="#fff"/><circle cx="10" cy="8.3" r="1.4" fill="#33a6d7"/></svg>514 - 23 St NE | T3K5M8</li>
  </ul>
</section>

<section class="card card--info-b">
  <div class="brand-name brand-name--small">REENA DHOT</div>
  <ul class="contact-list">
    <li><svg class="contact-icon" viewBox="0 0 20 20"><circle cx="10" cy="10" r="10" fill="#33a6d7"/><path d="M6.5 5.5l2 0 1 2.5-1.3 1a6 6 0 0 0 2.8 2.8l1-1.3 2.5 1v2a1 1 0 0 1-1 1A8 8 0 0 1 5.5 6.5a1 1 0 0 1 1-1z" fill="#fff"/></svg>Reena Dhot Office 4035550187</li>
    <li><svg class="contact-icon" viewBox="0 0 20 20"><circle cx="10" cy="10" r="10" fill="#33a6d7"/><path d="M6.5 5.5l2 0 1 2.5-1.3 1a6 6 0 0 0 2.8 2.8l1-1.3 2.5 1v2a1 1 0 0 1-1 1A8 8 0 0 1 5.5 6.5a1 1 0 0 1 1-1z" fill="#fff"/></svg>4035550264</li>
    <li><svg class="contact-icon" viewBox="0 0 20 20"><circle cx="10" cy="10" r="10" fill="#33a6d7"/><rect x="5" y="6.5" width="10" height="7" fill="none" stroke="#fff" stroke-width="1.2"/><path d="M5 6.5l5 4 5-4" fill="none" stroke="#fff" stroke-width="1.2"/></svg>Reena@ReenaDhot.Com</li>
    <li><svg class="contact-icon" viewBox="0 0 20 20"><circle cx="10" cy="10" r="10" fill="#33a6d7"/><circle cx="10" cy="10" r="5" fill="none" stroke="#fff" stroke-width="1.1"/><ellipse cx="10" cy="10" rx="2.2" ry="5" fill="none" stroke="#fff" stroke-width="1.1"/><path d="M5 10h10" stroke="#fff" stroke-width="1.1"/></svg>ReenaDhot.Com</li>
    <li><svg class="contact-icon" viewBox="0 0 20 20"><circle cx="10" cy="10" r="10" fill="#33a6d7"/></svg>RDhotRealty</li>
    <li><svg class="contact-icon" viewBox="0 0 20 20"><circle cx="10" cy="10" r="10" fill="#33a6d7"/></svg>Reena_Yyc_Realtor</li>
    <li><svg class="contact-icon" viewBox="0 0 20 20"><circle cx="10" cy="10" r="10" fill="#33a6d7"/><path d="M10 4.5a3.8 3.8 0 0 1 3.8 3.8c0 2.8-3.8 7-3.8 7s-3.8-4.2-3.8-7A3.8 3.8 0 0 1 10 4.5z" fill="#fff"/><circle cx="10" cy="8.3" r="1.4" fill="#33a6d7"/></svg>514 - 23 St NE | T3K5M8</li>
  </ul>
</section>

</body>
</html>
```